Law firm for traffic law - company portfolio

Company folder with logo and picture on the front. On the back only the imprint in DinA4 format. The following folders are ordered
https://www.falzhaus-kremvel.de/mappe-fuer-din-a4-2teilig-mit-2-laschen-40-farbig-aussseite-bedruck-mit-mattfolie-kaschiert.html#content-view

```html
<!DOCTYPE html>
<html lang="de">
<head>
<meta charset="utf-8">
<title>LEXVIA – Mappe Unfall-Management</title>
<link rel="stylesheet" href="https://fonts.googleapis.com/css2?family=Montserrat:wght@400;600;700;800&family=Open+Sans:ital,wght@0,400;0,600;0,700;1,700&display=swap">
<style>
:root{
  --navy:#1b3553;
  --navy-dark:#132840;
  --orange:#f39200;
  --white:#ffffff;
  --paper:#e8e9eb;
  --flap:#cfd4db;
  --text:#2c3a4a;
  --muted:#6b7785;
}
*{box-sizing:border-box;margin:0;padding:0}
html,body{width:818px;height:1200px;overflow:hidden}
body{background:var(--paper);font-family:"Open Sans",Arial,sans-serif;color:var(--text);position:relative}
.sheet{position:absolute;left:0;width:818px}
.sheet--outer{top:0;height:590px}
.sheet--inner{top:600px;height:600px}
.dieline{position:absolute;inset:0}
.abs{position:absolute}

/* outer back panel */
.back{left:32px;top:58px;width:374px;height:500px;background:var(--navy);overflow:hidden}
.back__web{left:0;top:0;width:40px;height:500px;background:var(--navy-dark)}
.back__web span{position:absolute;left:20px;top:250px;transform:translate(-50%,-50%) rotate(-90deg);white-space:nowrap;color:var(--white);font:600 13px/1 "Montserrat",sans-serif;letter-spacing:4px}
.section-title{font:800 15px/1.1 "Montserrat",sans-serif;color:var(--orange);letter-spacing:.5px}
.back .section-title{left:58px;top:34px}
.team{left:58px;top:64px;width:300px;display:grid;grid-template-columns:repeat(3,1fr);gap:14px 10px}
.person{display:flex;gap:5px;align-items:flex-start}
.person__dot{width:6px;height:6px;margin-top:3px;background:var(--orange);flex:none}
.person__name{font:700 7.5px/1.2 "Montserrat",sans-serif;color:var(--white)}
.person__role{font:400 6.5px/1.3 "Open Sans",sans-serif;color:#b9c4d1}
.back__divider{left:58px;top:258px;width:300px;height:2px;background:var(--orange)}
.brand{font:800 24px/1 "Montserrat",sans-serif;letter-spacing:1px;display:flex;align-items:center;gap:7px}
.brand__mark{width:10px;height:10px;background:var(--orange)}
.back .brand{left:58px;top:278px;color:var(--white)}
.back .kontakt{left:58px;top:316px;font:800 18px/1 "Montserrat",sans-serif;color:var(--white)}
.contacts{left:58px;top:348px;width:300px;display:grid;grid-template-columns:1fr 1fr;gap:10px 14px}
.contact{display:flex;align-items:center;gap:6px;color:var(--white);font:400 7.5px/1.3 "Open Sans",sans-serif}
.contact svg{flex:none}
.back__url{left:58px;top:420px;color:#b9c4d1;font:600 9px/1 "Montserrat",sans-serif;letter-spacing:1px}
.back__stripe{right:-20px;bottom:20px;width:140px;height:12px;background:var(--orange);transform:rotate(-28deg)}

/* outer front panel */
.front{left:406px;top:58px;width:384px;height:500px;background:var(--white);overflow:hidden}
.front__accent{left:0;top:0;width:384px;height:150px}
.front .brand{right:24px;top:22px;color:var(--navy);font-size:26px}
.front__title{right:24px;top:72px;text-align:right;font:800 16px/1.15 "Montserrat",sans-serif;color:var(--navy)}
.front__title span{display:block;color:var(--orange)}
.photo{left:0;top:138px;width:384px;height:275px;background:linear-gradient(160deg,#8f9aa6 0%,#6d7680 35%,#b33a2f 60%,#5a5f66 100%)}
.front__slogan{right:24px;top:430px;text-align:right;font:700 13px/1.3 "Montserrat",sans-serif;color:var(--navy)}
.front__band{left:0;bottom:0;width:384px;height:14px;background:var(--navy)}
.front__band::before{content:"";position:absolute;left:0;top:-4px;width:120px;height:4px;background:var(--orange)}

/* inner spread */
.inner{left:32px;top:26px;width:758px;height:470px;background:var(--white);overflow:hidden}
.inner__band{left:0;top:0;width:758px;height:56px;background:var(--navy)}
.inner__band .brand{left:50%;top:16px;transform:translateX(-50%);color:var(--white)}
.inner__band::after{content:"";position:absolute;left:0;bottom:-5px;width:758px;height:5px;background:var(--orange)}
.col{top:78px;width:340px}
.col--left{left:22px}
.col--right{left:392px}
.inner__fold{left:378px;top:70px;width:1px;height:390px;background:#dfe3e8}
.col .section-title{font-size:14px;color:var(--orange);margin-bottom:14px}
.quote{font:700 12.5px/1.3 "Montserrat",sans-serif;color:var(--navy);margin-bottom:6px}
.body{font:400 7.5px/1.45 "Open Sans",sans-serif;color:var(--muted);margin-bottom:10px}
.lead{font:700 10px/1.35 "Montserrat",sans-serif;color:var(--orange);margin-bottom:12px}
.sub{font:800 11px/1 "Montserrat",sans-serif;color:var(--navy);margin-bottom:8px}
.bullet{display:flex;gap:6px;font:700 10px/1.3 "Montserrat",sans-serif;color:var(--orange);margin-bottom:8px}
.bullet::before{content:"";width:6px;height:6px;margin-top:4px;background:var(--orange);flex:none}
.items{list-style:none;margin-left:12px}
.items li{font:400 7.5px/1.6 "Open Sans",sans-serif;color:var(--muted);padding-left:8px;position:relative}
.items li::before{content:"";position:absolute;left:0;top:5px;width:3px;height:3px;background:var(--orange)}
.check{display:flex;gap:7px;margin-bottom:12px}
.check svg{flex:none;margin-top:1px}
.check__title{font:700 11px/1.3 "Montserrat",sans-serif;color:var(--navy)}
.check__text{font:400 7.5px/1.4 "Open Sans",sans-serif;color:var(--muted);margin-top:2px}
.closing{font:700 11px/1.4 "Montserrat",sans-serif;color:var(--navy);margin-top:4px}
.closing span{display:block;color:var(--orange)}
</style>
</head>
<body>

<section class="sheet sheet--outer">
  <svg class="dieline" width="818" height="590" viewBox="0 0 818 590" aria-hidden="true">
    <polygon points="60,58 84,24 380,24 404,58" fill="var(--navy-dark)"/>
    <polygon points="436,58 460,24 760,24 788,58" fill="var(--flap)"/>
    <polygon points="32,90 10,110 10,520 32,540" fill="var(--flap)"/>
    <polygon points="790,90 808,112 808,510 790,530" fill="var(--flap)"/>
    <polygon points="60,558 84,582 380,582 404,558" fill="var(--flap)"/>
  </svg>

  <div class="abs back">
    <div class="abs back__web"><span>www.lexvia-recht.de</span></div>
    <h2 class="abs section-title">IHRE ANSPRECHPARTNER</h2>
    <div class="abs team">
      <div class="person"><i class="person__dot"></i><div><p class="person__name">LENA HARTWIG</p><p class="person__role">Rechtsanwältin</p></div></div>
      <div class="person"><i class="person__dot"></i><div><p class="person__name">JONAS BERGER</p><p class="person__role">Rechtsanwalt</p></div></div>
      <div class="person"><i class="person__dot"></i><div><p class="person__name">MIRA KESSLER</p><p class="person__role">Rechtsanwältin</p></div></div>
      <div class="person"><i class="person__dot"></i><div><p class="person__name">TOBIAS WENDT</p><p class="person__role">Rechtsanwalt</p></div></div>
      <div class="person"><i class="person__dot"></i><div><p class="person__name">SARA LINDNER</p><p class="person__role">Rechtsanwältin</p></div></div>
      <div class="person"><i class="person__dot"></i><div><p class="person__name">FELIX ROTH</p><p class="person__role">Rechtsanwalt</p></div></div>
      <div class="person"><i class="person__dot"></i><div><p class="person__name">NINA FALK</p><p class="person__role">Rechtsanwältin</p></div></div>
      <div class="person"><i class="person__dot"></i><div><p class="person__name">DAVID KRAUSE</p><p class="person__role">Rechtsanwalt</p></div></div>
      <div class="person"><i class="person__dot"></i><div><p class="person__name">ELIF AYDIN</p><p class="person__role">Rechtsanwältin</p></div></div>
      <div class="person"><i class="person__dot"></i><div><p class="person__name">MARC VOGEL</p><p class="person__role">Rechtsanwalt</p></div></div>
      <div class="person"><i class="person__dot"></i><div><p class="person__name">JULIA SOMMER</p><p class="person__role">Rechtsanwältin</p></div></div>
      <div class="person"><i class="person__dot"></i><div><p class="person__name">PAUL HEINZE</p><p class="person__role">Rechtsanwalt</p></div></div>
    </div>
    <div class="abs back__divider"></div>
    <div class="abs brand"><i class="brand__mark"></i>LEXVIA</div>
    <h2 class="abs kontakt">KONTAKTDATEN</h2>
    <div class="abs contacts">
      <div class="contact"><svg width="12" height="12" viewBox="0 0 24 24"><path d="M12 2a7 7 0 0 0-7 7c0 5 7 13 7 13s7-8 7-13a7 7 0 0 0-7-7zm0 9.5A2.5 2.5 0 1 1 12 6.5a2.5 2.5 0 0 1 0 5z" fill="var(--orange)"/></svg>Musterallee 14, 60311 Musterstadt</div>
      <div class="contact"><svg width="12" height="12" viewBox="0 0 24 24"><path d="M6.6 10.8a15 15 0 0 0 6.6 6.6l2.2-2.2a1 1 0 0 1 1-.25 11.4 11.4 0 0 0 3.6.57 1 1 0 0 1 1 1V20a1 1 0 0 1-1 1A17 17 0 0 1 3 4a1 1 0 0 1 1-1h3.5a1 1 0 0 1 1 1c0 1.25.2 2.45.57 3.57a1 1 0 0 1-.25 1z" fill="var(--orange)"/></svg>069 123 456 70</div>
      <div class="contact"><svg width="12" height="12" viewBox="0 0 24 24"><path d="M6.6 10.8a15 15 0 0 0 6.6 6.6l2.2-2.2a1 1 0 0 1 1-.25 11.4 11.4 0 0 0 3.6.57 1 1 0 0 1 1 1V20a1 1 0 0 1-1 1A17 17 0 0 1 3 4a1 1 0 0 1 1-1h3.5a1 1 0 0 1 1 1c0 1.25.2 2.45.57 3.57a1 1 0 0 1-.25 1z" fill="var(--orange)"/></svg>069 123 456 71</div>
      <div class="contact"><svg width="12" height="12" viewBox="0 0 24 24"><path d="M3 5h18v14H3z M3 5l9 7 9-7" fill="none" stroke="var(--orange)" stroke-width="2"/></svg>info@lexvia-recht.de</div>
    </div>
    <p class="abs back__url">www.lexvia-recht.de</p>
    <div class="abs back__stripe"></div>
  </div>

  <div class="abs front">
    <svg class="abs front__accent" width="384" height="150" viewBox="0 0 384 150" aria-hidden="true">
      <polygon points="0,0 110,0 40,140 0,140" fill="var(--navy)"/>
      <polygon points="118,0 136,0 66,140 48,140" fill="var(--orange)"/>
    </svg>
    <div class="abs brand"><i class="brand__mark"></i>LEXVIA</div>
    <h1 class="abs front__title">PROFESSIONELLES<span>UNFALL-MANAGEMENT</span></h1>
    <div class="abs photo" role="img" aria-label="Foto: beschädigtes rotes Auto nach einem Verkehrsunfall, daneben eine Person am Telefon"></div>
    <p class="abs front__slogan">Die Kompetente Abwicklung<br>Ihres Verkehrsunfalles</p>
    <div class="abs front__band"></div>
  </div>
</section>

<section class="sheet sheet--inner">
  <svg class="dieline" width="818" height="600" viewBox="0 0 818 600" aria-hidden="true">
    <polygon points="32,60 10,80 10,470 32,490" fill="var(--flap)"/>
    <polygon points="790,60 808,80 808,470 790,490" fill="var(--flap)"/>
    <polygon points="32,496 32,560 60,588 380,588 404,560 404,496" fill="var(--white)" stroke="var(--flap)" stroke-width="2"/>
    <polygon points="414,496 414,560 438,588 762,588 790,560 790,496" fill="var(--white)" stroke="var(--flap)" stroke-width="2"/>
    <polygon points="60,560 380,560 368,580 72,580" fill="var(--paper)"/>
    <polygon points="438,560 762,560 750,580 450,580" fill="var(--paper)"/>
  </svg>

  <div class="abs inner">
    <div class="abs inner__band"><div class="abs brand"><i class="brand__mark"></i>LEXVIA</div></div>
    <div class="abs inner__fold"></div>

    <div class="abs col col--left">
      <h2 class="section-title">PROFESSIONELLES<br>UNFALL-MANAGEMENT</h2>
      <p class="quote">" Verschenken Sie kein bares Geld! "</p>
      <p class="body">Nach einem Verkehrsunfall stehen Ihnen als Geschädigtem zahlreiche Ansprüche zu, die häufig nicht vollständig von der Versicherung reguliert werden.</p>
      <p class="lead">Wir sind die Vertrauensanwälte Ihres Autohauses und helfen Ihnen gern!</p>
      <p class="sub">UNSER SERVICE:</p>
      <p class="bullet">Wir ermitteln zielgerichtet alle Ihnen zustehenden Ansprüche, u.a.:</p>
      <p class="body">Unsere Kanzlei prüft jeden Fall individuell und setzt Ihre Forderungen konsequent durch.</p>
      <ul class="items">
        <li>Reparaturkosten</li>
        <li>Wiederbeschaffungswert</li>
        <li>Wertminderung</li>
        <li>Nutzungsausfall</li>
        <li>Sachverständigenkosten</li>
        <li>Mietwagenkosten</li>
        <li>Schmerzensgeld</li>
      </ul>
    </div>

    <div class="abs col col--right">
      <div class="check"><svg width="12" height="12" viewBox="0 0 24 24"><path d="M3 12l6 6L21 6" fill="none" stroke="var(--orange)" stroke-width="4"/></svg><div><p class="check__title">Wir übernehmen die gesamte Korrespondenz mit der Versicherung</p></div></div>
      <div class="check"><svg width="12" height="12" viewBox="0 0 24 24"><path d="M3 12l6 6L21 6" fill="none" stroke="var(--orange)" stroke-width="4"/></svg><div><p class="check__title">Unsere Beauftragung ist für Sie kostenfrei</p><p class="check__text">Die Kosten trägt in der Regel die gegnerische Versicherung.</p></div></div>
      <div class="check"><svg width="12" height="12" viewBox="0 0 24 24"><path d="M3 12l6 6L21 6" fill="none" stroke="var(--orange)" stroke-width="4"/></svg><div><p class="check__title">Verbrauchertest 9/2018</p><p class="check__text">Anwaltliche Vertretung senkt das Risiko einer Kürzung deutlich.</p></div></div>
      <div class="check"><svg width="12" height="12" viewBox="0 0 24 24"><path d="M3 12l6 6L21 6" fill="none" stroke="var(--orange)" stroke-width="4"/></svg><div><p class="check__title">OLG Musterstadt, Urteil vom 14.03.2016, Aktenzeichen 7U 204/15</p><p class="check__text">Die Kosten für das Anwaltsschreiben sind vom Schädiger zu ersetzen, auch bei eindeutiger Haftung.</p></div></div>
      <div class="check"><svg width="12" height="12" viewBox="0 0 24 24"><path d="M3 12l6 6L21 6" fill="none" stroke="var(--orange)" stroke-width="4"/></svg><div><p class="check__title">TV-Magazin Marktblick vom 25.07.2018</p><p class="check__text">Experten empfehlen frühzeitige anwaltliche Hilfe.</p></div></div>
      <div class="check"><svg width="12" height="12" viewBox="0 0 24 24"><path d="M3 12l6 6L21 6" fill="none" stroke="var(--orange)" stroke-width="4"/></svg><div><p class="check__title">Wir managen Ihren Verkehrsunfall, rufen Sie uns einfach an!</p></div></div>
      <p class="closing"><span>Ihr gutes Recht braucht Spezialisten!</span></p>
    </div>
  </div>
</section>

</body>
</html>
```